Design a For Sale sign board and Direction Sign Board.
Attached is an example of what i am thinking but am happy to look at any options.
Colours are to be ""bright Orange"on white and in reverse as well.

Logo id Fairbrook & Co Real Estate.

```html
<!DOCTYPE html>
<html lang="en">
<head>
<meta charset="utf-8">
<title>Fairbrook &amp; Co Real Estate – Direction Sign</title>
<link rel="stylesheet" href="https://fonts.googleapis.com/css2?family=Jost:wght@600&display=swap">
<style>
  :root {
    --sign-orange: #f7a21d;
    --arrow-black: #231f20;
    --sign-white: #ffffff;
    --backdrop: #eceae6;
  }
  * { margin: 0; padding: 0; box-sizing: border-box; }
  html, body {
    width: 1200px;
    height: 1200px;
    overflow: hidden;
    background: var(--backdrop);
  }
  .canvas {
    position: relative;
    width: 1200px;
    height: 1200px;
  }
  .direction-sign {
    position: absolute;
    left: 60px;
    top: 210px;
    width: 1080px;
    height: 780px;
  }
  .sign-board { fill: var(--sign-orange); }
  .brand-name,
  .brand-tagline,
  .agent-name {
    font-family: 'Jost', sans-serif;
    font-weight: 600;
    fill: var(--sign-white);
  }
  .brand-name { font-size: 118px; }
  .brand-tagline { font-size: 58px; letter-spacing: 10px; }
  .direction-arrow { fill: var(--arrow-black); }
  .agent-name { font-size: 136px; }
</style>
</head>
<body>
  <main class="canvas">
    <svg class="direction-sign" viewBox="0 0 1080 780" xmlns="http://www.w3.org/2000/svg">
      <rect class="sign-board" x="0" y="0" width="1080" height="780"/>

      <g class="brand-lockup">
        <text class="brand-name" x="540" y="225" text-anchor="middle">Fairbrook &amp; Co</text>
        <text class="brand-tagline" x="540" y="318" text-anchor="middle">REAL ESTATE</text>
      </g>

      <polygon class="direction-arrow"
        points="1080,491 297,510 297,452 53,585 297,696 297,655 1080,640"/>
      <text class="agent-name" x="194" y="632" textLength="830" lengthAdjust="spacingAndGlyphs">JANE PARKER</text>
    </svg>
  </main>
</body>
</html>
```